The Brandwell Group Billboard Design

The Brandwell Group is doing a Motorcycle Gordon campaign and we need a billboard design. The following are the requirements:

1. We need Gordon Brandwell, who is in the photo attached, to be photoshopped into a black leather three-piece suit, white hair and beard, next to a really cool old school Tarvin Rourke motorcycle, with a South Carolina scene in the background.
2. The Billboard should have the slogan "Motorcycle Wreck? We have your back!"
3. Our logo, which is attached, needs to be on the billboard
4. Our phone number needs to be on the billboard - (555) 274-6190
5. Tarvin Rourke colors

```html
<!DOCTYPE html>
<html lang="en">
<head>
<meta charset="utf-8">
<title>The Brandwell Group Billboard</title>
<link href="https://fonts.googleapis.com/css2?family=Montserrat:wght@600;700;800;900&display=swap" rel="stylesheet">
<style>
  :root {
    --page-bg: #e9eaec;
    --board-bg: #2a2a2c;
    --orange: #f7941d;
    --white: #ffffff;
    --ink: #1d1d1f;
    --photo-light: #8e9aa4;
    --photo-dark: #4a4f55;
  }
  * { margin: 0; padding: 0; box-sizing: border-box; }
  html, body {
    width: 1200px;
    height: 2204px;
    overflow: hidden;
    background: var(--page-bg);
    font-family: "Montserrat", Arial, sans-serif;
  }
  .billboard {
    position: absolute;
    left: 50px;
    top: 860px;
    width: 1100px;
    height: 484px;
    background: var(--board-bg);
    overflow: hidden;
  }
  .hero-photo {
    position: absolute;
    left: 0;
    top: 0;
    width: 620px;
    height: 484px;
  }
  .copy {
    position: absolute;
    left: 636px;
    top: 38px;
    width: 440px;
  }
  .brand {
    display: flex;
    flex-direction: column;
    align-items: center;
    width: 420px;
  }
  .brand-name {
    color: var(--orange);
    font-weight: 700;
    font-size: 48px;
    letter-spacing: 2px;
    line-height: 1;
  }
  .brand-tagline {
    color: var(--white);
    font-weight: 600;
    font-size: 9.5px;
    letter-spacing: 0.6px;
    margin-top: 6px;
    white-space: nowrap;
  }
  .headline {
    margin-top: 26px;
    line-height: 0.95;
    font-weight: 900;
  }
  .headline-top {
    display: block;
    color: var(--orange);
    font-size: 58px;
    white-space: nowrap;
  }
  .headline-bottom {
    display: block;
    color: var(--white);
    font-size: 82px;
  }
  .slogan {
    margin-top: 12px;
    color: var(--orange);
    font-weight: 700;
    font-size: 36px;
    white-space: nowrap;
  }
  .phone-band {
    position: absolute;
    left: 600px;
    top: 370px;
    width: 500px;
    height: 84px;
    background: var(--orange);
    display: flex;
    align-items: center;
    padding-left: 34px;
  }
  .phone-number {
    color: var(--ink);
    font-weight: 800;
    font-size: 56px;
    letter-spacing: -0.5px;
    white-space: nowrap;
  }
</style>
</head>
<body>
  <section class="billboard">
    <svg class="hero-photo" viewBox="0 0 620 484" role="img" aria-label="Photo of Gordon Brandwell in a black leather suit seated on a classic black Tarvin Rourke motorcycle, South Carolina scenery behind">
      <defs>
        <linearGradient id="photo-tone" x1="0" y1="0" x2="1" y2="1">
          <stop offset="0" stop-color="var(--photo-light)"/>
          <stop offset="1" stop-color="var(--photo-dark)"/>
        </linearGradient>
      </defs>
      <path d="M0 0 H480 A140 140 0 0 1 620 140 V484 H0 Z" fill="url(#photo-tone)"/>
    </svg>

    <div class="copy">
      <div class="brand">
        <span class="brand-name">BRANDWELL</span>
        <span class="brand-tagline">SOUTH CAROLINA MOTORCYCLE WRECK LAWYERS</span>
      </div>
      <h1 class="headline">
        <span class="headline-top">MOTORCYCLE</span>
        <span class="headline-bottom">WRECK?</span>
      </h1>
      <p class="slogan">We have your back!</p>
    </div>

    <div class="phone-band">
      <span class="phone-number">(555) 274-6190</span>
    </div>
  </section>
</body>
</html>
```